Northern Peak Claims Service needs a business card design

We need a business card design for a medical billing service, located in Anchorage, AK. We provide medical claims billing and management to Alaskan medical practices/clinics. We would like to see designs that depict Alaskan Mountain Ranges, or water features, or trees. An outdoorsy feel, perhaps. Not exactly sure.

Industry/Entity Type

Medical

```html
<!DOCTYPE html>
<html lang="en">
<head>
<meta charset="utf-8">
<title>Northern Peak Claims Service – Business Card</title>
<link rel="stylesheet" href="https://fonts.googleapis.com/css2?family=Noto+Serif:wght@700&family=Questrial&display=swap">
<style>
  :root {
    --bg: #ece8e2;
    --blue-light: #4a4fd0;
    --blue-dark: #2a2eab;
    --red-light: #ea3038;
    --red-dark: #c5161f;
    --white: #ffffff;
    --navy: #3436a8;
    --title-yellow: #f4e23a;
    --icon-red: #e2242c;
  }
  * { margin: 0; padding: 0; box-sizing: border-box; }
  html, body { width: 1200px; height: 1000px; overflow: hidden; }
  body { background: var(--bg); position: relative; font-family: "Questrial", sans-serif; }

  .card {
    position: absolute;
    left: 250px;
    width: 700px;
    height: 400px;
    overflow: hidden;
    box-shadow: 0 6px 18px rgba(0,0,0,0.18);
  }
  .card--front { top: 60px; background: linear-gradient(135deg, var(--blue-light), var(--blue-dark)); }
  .card--back { top: 540px; background: linear-gradient(135deg, var(--red-light), var(--red-dark)); }

  .card__shapes { position: absolute; inset: 0; }

  .brand {
    position: absolute;
    left: 75px;
    top: 105px;
    width: 290px;
    height: 160px;
    display: flex;
    align-items: center;
    justify-content: center;
    gap: 14px;
  }
  .brand__dot { width: 26px; height: 26px; border-radius: 50%; background: var(--navy); flex: none; }
  .brand__name {
    color: var(--navy);
    font-family: "Questrial", sans-serif;
    font-size: 25px;
    line-height: 1.15;
    letter-spacing: 0.5px;
    text-transform: uppercase;
    width: 200px;
  }

  .contact { position: absolute; left: 410px; top: 50px; color: var(--white); }
  .contact__name { font-family: "Noto Serif", serif; font-weight: 700; font-size: 25px; }
  .contact__title { color: var(--title-yellow); font-size: 16px; margin: 4px 0 12px; }
  .contact__list { list-style: none; }
  .contact__item { display: flex; align-items: center; gap: 10px; font-size: 17px; margin-bottom: 6px; }
  .contact__icon { width: 19px; height: 19px; flex: none; }

  .tagline {
    position: absolute;
    left: 24px;
    right: 24px;
    bottom: 14px;
    color: var(--white);
    font-size: 16px;
    letter-spacing: 0.2px;
    white-space: nowrap;
  }

  .back__url {
    position: absolute;
    left: 420px;
    top: 300px;
    color: var(--white);
    font-size: 20px;
  }
</style>
</head>
<body>

<section class="card card--front" aria-label="Business card front">
  <svg class="card__shapes" width="700" height="400" viewBox="0 0 700 400" aria-hidden="true">
    <rect x="0" y="0" width="60" height="350" fill="var(--white)"/>
    <circle cx="220" cy="185" r="165" fill="var(--white)"/>
  </svg>

  <div class="brand">
    <span class="brand__dot"></span>
    <span class="brand__name">Northern Peak Claims Service</span>
  </div>

  <div class="contact">
    <p class="contact__name">Your name here</p>
    <p class="contact__title">Title here</p>
    <ul class="contact__list">
      <li class="contact__item">
        <svg class="contact__icon" viewBox="0 0 20 20" aria-hidden="true"><rect width="20" height="20" rx="2" fill="var(--icon-red)"/><rect x="5" y="4" width="10" height="12" rx="1" fill="none" stroke="#fff" stroke-width="1.6"/><rect x="7" y="6" width="6" height="3" fill="#fff"/></svg>
        <span>(555)010-2147</span>
      </li>
      <li class="contact__item">
        <svg class="contact__icon" viewBox="0 0 20 20" aria-hidden="true"><rect width="20" height="20" rx="2" fill="var(--icon-red)"/><path d="M6 4 L8.5 4 L9.5 7 L8 8.3 C8.8 10 10 11.2 11.7 12 L13 10.5 L16 11.5 L16 14 C11 14.5 5.5 9 6 4 Z" fill="#fff"/></svg>
        <span>(555)010-3861</span>
      </li>
      <li class="contact__item">
        <svg class="contact__icon" viewBox="0 0 20 20" aria-hidden="true"><rect width="20" height="20" rx="2" fill="var(--icon-red)"/><rect x="4" y="6" width="12" height="8" fill="none" stroke="#fff" stroke-width="1.5"/><path d="M4 6 L10 11 L16 6" fill="none" stroke="#fff" stroke-width="1.5"/></svg>
        <span>hello@northpeakclaims.com</span>
      </li>
      <li class="contact__item">
        <svg class="contact__icon" viewBox="0 0 20 20" aria-hidden="true"><rect width="20" height="20" rx="2" fill="var(--icon-red)"/><circle cx="10" cy="10" r="6" fill="none" stroke="#fff" stroke-width="1.5"/><ellipse cx="10" cy="10" rx="2.6" ry="6" fill="none" stroke="#fff" stroke-width="1.2"/><line x1="4" y1="10" x2="16" y2="10" stroke="#fff" stroke-width="1.2"/></svg>
        <span>www.northpeakclaims.com</span>
      </li>
    </ul>
  </div>

  <p class="tagline">Medical claims billing and management to Alaskan medical practices/clinics</p>
</section>

<section class="card card--back" aria-label="Business card back">
  <svg class="card__shapes" width="700" height="400" viewBox="0 0 700 400" aria-hidden="true">
    <rect x="0" y="0" width="60" height="350" fill="var(--white)"/>
    <circle cx="220" cy="185" r="165" fill="var(--white)"/>
  </svg>

  <div class="brand">
    <span class="brand__dot"></span>
    <span class="brand__name">Northern Peak Claims Service</span>
  </div>

  <p class="back__url">www.northpeakclaims.com</p>
</section>

</body>
</html>
```